2 banner Designs

I have a trade show in Vegas and I want you to design 2 banners that are Graphic size: 33.5" (W) x 80.5" (H). The banners are standing in the booth.

I am looking for a luxury modern feel for the banners. The banners are going to be important to attract customers in.

I am showing latex foam pillows and latex mattress. The company is called Verdant Rest. Please use any photos from our website.

https://www.lumivaslee.net/verdantrest

Banner 1

Introducing our Verdant Rest mattress, a perfect harmony of luxurious organic cushioning and an advanced internal, zoned pressure-point support system.

Experience unparalleled back support and remarkable durability, all in one exceptional sleep solution.

Verdant Rest Mattress

HVRA-certified organic cotton
HVRA-certified organic wool
2 “ HVLA-certified organic latex
8” Pocket Coils
1’’ HVLA-certified organic latex

Banner 2

Verdant Rest Pillows

We developed a customizable pillow with the perfect amount of comfort and support.

Our New Latex pillow has an adjustable fill with 90% Natural Latex and 10% Traceable Wool.  Our pillow cover is made from HVRA-certified organic cotton.

FILE REQUIREMENTS
We can take the file in the following file formats:

Single Page PDF (Preferred)
JPG (Preferred)
PSD – Please flatten file
EPS – Please embed all images. Outline all fonts and strokes.
Ai – Please embed all images. Outline all fonts and strokes.
Don't Include Crop Marks or Bleed

Artwork at either full scale, 1/2 scale or 1/10 scale that is fine. Just make sure that when the file is being set up the DPI is compensated according to the scale.

Full Scale – 150 DPI
1/2 Scale – 300 DPI
1/10 Scale – 450 DPI
***Remove EVERYTHING from your file that you do not want printed on the final product - especially hidden layers and template guidelines.

- Flatten all Objects/Gradients/Swatches/Symbols/Special Effects/Transparencies
- Outline all text
- Flattened PDF (Single Page) or JPEG file types only
- Remove all crop marks/bleed otherwise they will be printed
- File must be the same exact size as what is ordered (exception is Gallery wrap Fold Edge and Products with templates)
- CMYK only (we do not print Pantone/5th/Spot/RGB)
- 150 dpi
- If using a template, the file uploaded to our site should match the exact "template size" (different than "graphic size").
- Do not scale template files, just flatten them and save at 150 dpi
- Files over 200" can be scaled
- Under 300 mb for upload

- Make sure all objects are embedded and flattened (we do not print Non-Native Art).
- If the file is made in Indesign, please flatten the file in Illustrator or Photoshop and export to a JPEG ONLY as we don't recommend using Indesign at our facility.

- If using Compound Paths to create transparencies/shapes, please completely rasterize or flatten them into the file or they may print incorrectly.

- We do not have specific measurements for Panel jobs. If you are printing in Panels, please make sure you are providing a minimum of 1" overlay in your files.

Please make sure that your file is in CMYK format for print production with no bleed. It is not required.

```html
<!DOCTYPE html>
<html lang="en">
<head>
<meta charset="utf-8">
<title>Verdant Rest – Trade Show Banners</title>
<link href="https://fonts.googleapis.com/css2?family=Crimson+Text:wght@400;600&family=Mulish:wght@300&display=swap" rel="stylesheet">
<style>
  :root {
    --page: #efefed;
    --card: #ffffff;
    --sage: #8a957e;
    --leaf: #6a8a34;
    --leaf-fade: rgba(106,138,52,0);
    --ink: #2b2b2b;
    --cream: #f3eee4;
    --wood: #b88a66;
    --on-sage: #ffffff;
  }
  * { margin: 0; padding: 0; box-sizing: border-box; }
  html, body { width: 1102px; height: 1200px; overflow: hidden; }
  body { background: var(--page); position: relative; font-family: "Crimson Text", Georgia, serif; }

  .banner { position: absolute; top: 100px; width: 406px; height: 979px; background: var(--card); }
  .banner--mattress { left: 106px; }
  .banner--pillow { left: 585px; }

  .hero { position: absolute; left: 17px; top: 17px; width: 371px; background: var(--sage); overflow: hidden; }
  .banner--mattress .hero { height: 626px; }
  .banner--pillow .hero { height: 785px; }

  .hero__photo { position: absolute; left: 0; width: 100%; }
  .banner--mattress .hero__photo {
    top: 360px; height: 266px;
    background: linear-gradient(180deg, var(--sage) 0%, #d9ddd2 30%, #f2f2ee 60%, #e4e8df 100%);
  }
  .banner--pillow .hero__photo {
    top: 165px; height: 620px;
    background:
      radial-gradient(ellipse 45% 40% at 40% 60%, #f6f1e6 0%, rgba(246,241,230,0) 100%),
      linear-gradient(90deg, rgba(0,0,0,0) 70%, rgba(184,138,102,.55) 100%),
      linear-gradient(180deg, var(--sage) 0%, #c9cdbf 22%, #ece7dc 45%, var(--cream) 100%);
  }

  .hero__copy { position: absolute; color: var(--on-sage); font-size: 22px; line-height: 27.5px; }
  .banner--mattress .hero__copy { left: 38px; top: 24px; width: 320px; }
  .banner--pillow .hero__copy { left: 36px; top: 30px; width: 330px; line-height: 28.5px; }
  .hero__title { font-weight: 400; font-size: 37px; line-height: 44px; }
  .banner--pillow .hero__title { font-size: 41px; line-height: 44px; }
  .hero__copy p + p { margin-top: 27px; }

  .name-bar {
    position: absolute; left: 17px; height: 42px;
    background: linear-gradient(90deg, var(--leaf) 0%, var(--leaf) 82%, var(--leaf-fade) 100%);
    color: var(--on-sage); font-size: 22px; font-weight: 600; line-height: 42px; padding-left: 38px;
  }
  .banner--mattress .name-bar { top: 641px; width: 333px; }
  .banner--pillow .name-bar { top: 760px; width: 330px; padding-left: 29px; }

  .spec-list { position: absolute; left: 53px; top: 705px; list-style: none;
    font-family: "Mulish", Arial, sans-serif; font-weight: 300; font-size: 16px; line-height: 21.5px; color: var(--ink); }

  .brand { position: absolute; left: 0; width: 100%; display: flex; justify-content: center; align-items: center; gap: 10px;
    color: var(--leaf); font-size: 34px; font-weight: 400; }
  .banner--mattress .brand { top: 860px; }
  .banner--pillow .brand { top: 862px; }
  .brand__dot { width: 14px; height: 14px; border-radius: 50%; background: var(--leaf); }
</style>
</head>
<body>
  <section class="banner banner--mattress">
    <div class="hero">
      <div class="hero__photo" role="img" aria-label="Photo of the Verdant Rest mattress on a dark grey base"></div>
      <div class="hero__copy">
        <p><span class="hero__title">Introducing</span><br>our Verdant Rest mattress, a perfect harmony of luxurious organic cushioning and an advanced internal, zoned pressure-point support system.</p>
        <p>Experience unparalleled back support and remarkable durability, all in one exceptional sleep solution.</p>
      </div>
    </div>
    <div class="name-bar">Verdant Rest Mattress</div>
    <ul class="spec-list">
      <li>HVRA-certified organic cotton</li>
      <li>HVRA-certified organic wool</li>
      <li>2 ″ HVLA-certified organic latex</li>
      <li>8″ Pocket Coils</li>
      <li>1″ HVLA-certified organic latex</li>
    </ul>
    <div class="brand"><span class="brand__dot"></span>Verdant Rest</div>
  </section>

  <section class="banner banner--pillow">
    <div class="hero">
      <div class="hero__photo" role="img" aria-label="Photo of a smiling woman hugging a latex pillow on a bed"></div>
      <div class="hero__copy">
        <p><span class="hero__title">Our new latex</span><br>pillow has an adjustable fill with 90% natural latex and 10% traceable wool. Our pillow cover is made from HVRA-certified organic cotton.</p>
      </div>
    </div>
    <div class="name-bar">Verdant Rest Pillows</div>
    <div class="brand"><span class="brand__dot"></span>Verdant Rest</div>
  </section>
</body>
</html>
```